Fitness Equipment Repair Business Needs a Catchy New Business Card

We have an existing business card, however, it is quite plain and boring. We are expanding primarily in the commercial area (gyms, studios, apartment complexes etc). The business card will serve as eye candy to those managers/owners that can't be met for a face to face.
Originally I was planning for a brochure as well, but all of our information is better summarized on our website. (brookmotionservice.ca).
I would like the card to match the colour scheme of the website and utilize the logo. It should have a professional clean feel to it, however, a little colouring outside the lines wouldn't hurt.
The example card is for my service technician (Colin Harstad). If possible I would like to be able to edit the text to use for more than one person.

Industry/Entity Type

Appliance Repair

Contact Information for Business Card

Clean, crisp and professional but needs to be eye catching. Preferably using the black, white and red colour scheme matching the website. Double sided would be nice, but is not necessary.

Colors
ec1f27
ffffff
000000

Requirements
Must have
• Must be able to edit name, phone number and title to use for multiple people. Must show the company website (brookmotionservice.ca).

```html
<!DOCTYPE html>
<html lang="en">
<head>
<meta charset="utf-8">
<title>Brook Motion Service – Business Card</title>
<link href="https://fonts.googleapis.com/css2?family=Arvo:ital,wght@0,400;0,700;1,400&display=swap" rel="stylesheet">
<style>
  :root {
    --brand-red: #ec1f27;
    --brand-white: #ffffff;
    --brand-black: #000000;
    --stage: #3a3431;
    --line-grey: #8a8a8a;
    --art-tone: #1c1c1c;
  }
  * { box-sizing: border-box; margin: 0; padding: 0; }
  html, body { width: 1200px; height: 780px; overflow: hidden; }
  body {
    background: var(--stage);
    font-family: "Arvo", Georgia, serif;
    display: flex;
    align-items: center;
    justify-content: center;
    gap: 60px;
  }
  .card {
    position: relative;
    width: 525px;
    height: 300px;
    background: var(--brand-black);
    color: var(--brand-white);
    box-shadow: 0 14px 30px rgba(0,0,0,.45);
    overflow: hidden;
  }
  .mascot-art {
    position: absolute;
    width: 150px;
    height: 150px;
    border-radius: 6px;
    background: radial-gradient(circle at 50% 40%, #2d2d2d, var(--art-tone) 70%);
  }
  .company-name {
    position: absolute;
    width: 220px;
    text-align: center;
    font-size: 14px;
    font-weight: 400;
    letter-spacing: 1px;
    color: var(--brand-white);
    line-height: 1;
  }
  /* front */
  .card-front .mascot-art { left: 188px; top: 30px; }
  .card-front .company-name { left: 153px; top: 194px; }
  .tagline {
    position: absolute;
    left: 0; right: 0;
    top: 242px;
    text-align: center;
    font-size: 12.5px;
    font-style: italic;
    color: var(--brand-white);
  }
  /* back */
  .card-back .mascot-art { left: 50px; top: 50px; }
  .card-back .company-name { left: 15px; top: 216px; }
  .divider {
    position: absolute;
    left: 250px; top: 60px;
    width: 1px; height: 180px;
    background: var(--line-grey);
  }
  .contact {
    position: absolute;
    left: 280px; top: 60px;
    font-size: 13px;
    line-height: 1.45;
  }
  .person-name { font-size: 18px; font-weight: 700; line-height: 1.1; }
  .person-title { color: var(--brand-red); font-size: 13px; margin-bottom: 10px; }
  .address { margin-bottom: 8px; }
  .contact-line { display: flex; align-items: center; gap: 8px; }
  .contact-line svg { width: 13px; height: 13px; fill: var(--brand-red); flex: none; }
  .website { margin-top: 8px; }
  .website .domain { color: var(--brand-red); }
</style>
</head>
<body>
  <section class="card card-front">
    <div class="mascot-art" role="img" aria-label="Line illustration of a muscular technician in a hard hat holding a wrench"></div>
    <div class="company-name">Brook Motion Service</div>
    <p class="tagline">when your equipment can't finish the workout, give us a call !</p>
  </section>

  <section class="card card-back">
    <div class="mascot-art" role="img" aria-label="Line illustration of a muscular technician in a hard hat holding a wrench"></div>
    <div class="company-name">Brook Motion Service</div>
    <div class="divider"></div>
    <div class="contact">
      <div class="person-name">Colin Harstad</div>
      <div class="person-title">service technician</div>
      <div class="address">1875 Larkfield Road NW<br>Edmonton AB T5K 2P4</div>
      <div class="contact-line">
        <svg viewBox="0 0 16 16" aria-hidden="true"><rect x="4" y="1" width="8" height="14" rx="1.5"/><rect x="5.5" y="3" width="5" height="8" fill="#000"/></svg>
        <span>578-555-0142</span>
      </div>
      <div class="contact-line">
        <svg viewBox="0 0 16 16" aria-hidden="true"><path d="M1 5c0-2 3-3 7-3s7 1 7 3v1h-4V5H5v1H1z"/><rect x="3" y="7" width="10" height="7" rx="1"/></svg>
        <span>780-555-0187</span>
      </div>
      <div class="contact-line">
        <svg viewBox="0 0 16 16" aria-hidden="true"><rect x="1" y="3" width="14" height="10"/><path d="M1 3l7 6 7-6" fill="none" stroke="#000" stroke-width="1.3"/></svg>
        <span>service@brookmotion.ca</span>
      </div>
      <div class="website">www.<span class="domain">brookmotionservice</span>.ca</div>
    </div>
  </section>
</body>
</html>
```